Salon and Spa Distributor Business Card

Need a business card. We are are distributor in the salon and spa industry. We identify with natural beauty. Need a card with:
Company Name: Petal Haven"
Title: "President & CEO"
Address
Company Phone number
email
website
Tag Line:" The Professional Salon Source"

Industry/Entity Type

Business

Contact Information for Business Card

Name: Lena Morcott
Title: "President & CEO"
Address: 317 Birchfield Ln, Oakvane, NJ 07481
Company Phone number: 800-463-9152
email: lenamorcott@petalhaven-example.com
website: www.petalhaven-example.com

Requirements
Should not have
• No black backgrounds

```html
<!DOCTYPE html>
<html lang="en">
<head>
<meta charset="utf-8">
<title>Petal Haven — Business Card</title>
<link rel="stylesheet" href="https://fonts.googleapis.com/css2?family=Mulish:wght@300;400;500&family=Pinyon+Script&display=swap">
<style>
  :root {
    --stage: #000000;
    --paper: #ffffff;
    --green-light: #66bd48;
    --green-mid: #3f9a40;
    --green-dark: #137037;
    --text-green: #3a9440;
    --script-white: #ffffff;
  }
  * { box-sizing: border-box; margin: 0; padding: 0; }
  html, body { width: 1200px; height: 1000px; overflow: hidden; background: var(--stage); }
  .stage { position: relative; width: 1200px; height: 1000px; }

  .card {
    position: absolute; left: 258px; width: 684px; height: 391px;
    border-radius: 38px; overflow: hidden; background: var(--paper);
  }
  .card--front {
    top: 92px;
    background: linear-gradient(90deg, var(--paper) 0 35.5%, var(--green-light) 35.5%, var(--green-mid) 70%, var(--green-dark) 100%);
  }
  .card--back { top: 526px; }

  .artwork { position: absolute; }
  .card--front .artwork {
    left: 0; top: 0; width: 370px; height: 391px;
    background: linear-gradient(160deg, #ffffff 0%, #bfe3a9 35%, var(--green-light) 65%, #2f8a3b 100%);
    border-radius: 0 60% 45% 0 / 0 50% 50% 0;
  }
  .card--back .artwork {
    left: 330px; top: 0; width: 354px; height: 391px;
    background: linear-gradient(110deg, #c9e8b6 0%, var(--green-light) 35%, var(--green-mid) 65%, var(--green-dark) 100%);
    clip-path: polygon(38% 0, 100% 0, 100% 100%, 30% 100%, 22% 78%, 0 48%, 10% 22%);
  }

  .brand-name {
    position: absolute; font-family: "Mulish", sans-serif; font-weight: 300; white-space: nowrap;
  }
  .card--front .brand-name { left: 342px; top: 56px; font-size: 42px; color: var(--paper); }

  .tagline {
    position: absolute; left: 380px; top: 150px; width: 280px; text-align: center;
    font-family: "Pinyon Script", cursive; color: var(--script-white); line-height: 1;
  }
  .tagline span { display: block; }
  .tagline .t-the { font-size: 36px; }
  .tagline .t-professional { font-size: 46px; margin-top: 6px; }
  .tagline .t-salon { font-size: 52px; margin-top: 4px; }
  .tagline .t-source { font-size: 34px; margin-top: 4px; }

  .brand-block { position: absolute; left: 30px; top: 48px; display: flex; align-items: center; gap: 14px; }
  .brand-dot { width: 92px; height: 92px; border-radius: 50%; background: var(--green-light); flex: none; }
  .card--back .brand-name { position: static; font-size: 30px; font-weight: 400; color: var(--text-green); line-height: 1.1; }
  .job-title { font-family: "Mulish", sans-serif; font-size: 18px; font-weight: 500; color: var(--text-green); margin-top: 2px; }

  .contact { position: absolute; left: 25px; top: 246px; font-family: "Mulish", sans-serif; color: var(--text-green); font-size: 18px; z-index: 1; }
  .contact-row { display: flex; align-items: center; gap: 10px; height: 26px; white-space: nowrap; }
  .contact-row svg { width: 18px; height: 18px; flex: none; }
  .address { margin-top: 16px; white-space: nowrap; }
</style>
</head>
<body>
<main class="stage">

  <section class="card card--front" aria-label="Business card front">
    <div class="artwork" role="img" aria-label="Illustration of a woman's profile with flowing hair and leaves, in green tones"></div>
    <h1 class="brand-name">Petal Haven</h1>
    <p class="tagline">
      <span class="t-the">The</span>
      <span class="t-professional">Professional</span>
      <span class="t-salon">Salon</span>
      <span class="t-source">Source</span>
    </p>
  </section>

  <section class="card card--back" aria-label="Business card back">
    <div class="artwork" role="img" aria-label="Large illustration of a woman's profile with flowing hair and leaves, in green tones"></div>

    <div class="brand-block">
      <span class="brand-dot"></span>
      <div>
        <h2 class="brand-name">Petal Haven</h2>
        <p class="job-title">President &amp; CEO</p>
      </div>
    </div>

    <div class="contact">
      <div class="contact-row">
        <svg viewBox="0 0 18 18" aria-hidden="true"><rect x="4" y="1" width="10" height="16" rx="1.5" fill="none" stroke="currentColor" stroke-width="1.8"/><circle cx="9" cy="14" r="1" fill="currentColor"/></svg>
        <span>800-463-9152</span>
      </div>
      <div class="contact-row">
        <svg viewBox="0 0 18 18" aria-hidden="true"><rect x="1" y="3.5" width="16" height="11" fill="none" stroke="currentColor" stroke-width="1.8"/><path d="M1.5 4l7.5 6 7.5-6" fill="none" stroke="currentColor" stroke-width="1.6"/></svg>
        <span>lenamorcott@petalhaven-example.com</span>
      </div>
      <div class="contact-row">
        <svg viewBox="0 0 18 18" aria-hidden="true"><circle cx="9" cy="9" r="7.5" fill="none" stroke="currentColor" stroke-width="1.6"/><ellipse cx="9" cy="9" rx="3.2" ry="7.5" fill="none" stroke="currentColor" stroke-width="1.3"/><path d="M1.5 9h15M2.8 5h12.4M2.8 13h12.4" stroke="currentColor" stroke-width="1.2"/></svg>
        <span>www.petalhaven-example.com</span>
      </div>
      <p class="address">317 Birchfield Ln, Oakvane, NJ 07481</p>
    </div>
  </section>

</main>
</body>
</html>
```